Consulting, Investors, Joint Venture Website

Founded in April 2018, Marendo Consultants Limited (MCL) is an advisory consulting firm specializing in engaging investors in business ventures in Tanzania.
With extensive experience in construction, energy, oil and gas and the legal professions, our team assembles our expertise that allows foreign investors to set foot and flourish in the Tanzanian market.
MCL is locally owned, founded and registered. Our shareholders are cultured Tanzanian citizens with extensive corporate experience in South Africa, Tanzania, United Kingdom and the United States.

Our mission is to provide responsive and unrivalled professional advice from learned and experienced professionals versed in the local market, with an understanding of the cultural and logistical challenges faced by foreign investors.

Our vision is to provide a complete investor’s package that initiates with company registration, compliance and documentation services and ultimately operational facilitation services.

Target Market(s)

Foreign Investors, International companies

Industry/Entity Type

Business Consultant

Number of Pages Required

5+ page

Requirements
Must have
• It will be 5 pages - Home, About Us, Services, Portfolio, Contact Us
Nice to have
• if it can look like https://www.plorvex.example/
• or https://www.dunetri.example or http://www.quillbrook.example/

```html
<!DOCTYPE html>
<html lang="en">
<head>
<meta charset="utf-8">
<title>Marendo Consultants Limited – About Us</title>
<link href="https://fonts.googleapis.com/css2?family=Raleway:wght@400;500;600;700&display=swap" rel="stylesheet">
<style>
  :root {
    --navy: #1b4c9b;
    --text-blue: #2f5ea6;
    --orange: #f3911f;
    --white: #ffffff;
    --panel-shadow: 0 4px 14px rgba(20, 40, 80, 0.18);
    --field-line: #f5b77a;
    --muted: #7c8796;
  }
  * { box-sizing: border-box; margin: 0; padding: 0; }
  html, body { width: 1200px; height: 2946px; overflow: hidden; }
  body {
    position: relative;
    background: var(--white);
    font-family: "Raleway", Arial, sans-serif;
    color: var(--text-blue);
  }
  .abs { position: absolute; }

  /* Header */
  .brand { display: flex; align-items: center; gap: 10px; color: var(--navy); font-weight: 700; }
  .brand-mark { width: 34px; height: 34px; background: var(--navy); }
  .brand-name { line-height: 1; letter-spacing: 1px; }
  .brand-name small { display: block; font-size: 0.42em; letter-spacing: 3px; margin-top: 3px; }
  .site-header .brand { left: 40px; top: 32px; font-size: 34px; }
  .nav { left: 300px; top: 44px; display: flex; gap: 0; font-size: 15px; font-weight: 500; color: var(--navy); }
  .nav a { position: absolute; white-space: nowrap; color: inherit; text-decoration: none; }
  .nav a.active { font-weight: 700; }
  .nav a.active::after { content: ""; position: absolute; left: 18px; right: 18px; bottom: -12px; height: 2px; background: var(--orange); }
  .contact-btn { left: 676px; top: 28px; width: 135px; height: 51px; border-radius: 26px; background: var(--orange); color: var(--white); font-size: 15px; font-weight: 500; display: flex; align-items: center; justify-content: center; }
  .header-mail { left: 825px; top: 42px; display: flex; align-items: center; gap: 10px; font-size: 15px; font-weight: 600; color: var(--navy); }
  .header-social { left: 1027px; top: 38px; display: flex; gap: 7px; }
  .header-social span { width: 28px; height: 28px; background: var(--navy); display: block; }

  /* Hero */
  .hero { left: 0; top: 0; width: 1200px; height: 610px;
    background:
      linear-gradient(180deg, rgba(255,255,255,0.97) 0%, rgba(255,255,255,0.75) 16%, rgba(255,255,255,0) 45%),
      linear-gradient(90deg, #a7c3dc 0%, #e9d4b0 35%, #f2e0c0 55%, #b9c2c8 80%, #8fa4b3 100%); }

  /* Cards */
  .card { background: var(--white); box-shadow: var(--panel-shadow); }
  .about-card { left: 41px; top: 425px; width: 1118px; height: 631px; }
  .about-logo { left: 0; top: 0; width: 366px; height: 132px; display: flex; align-items: center; padding-left: 18px; }
  .about-logo .brand { font-size: 38px; }
  .about-photo { left: 0; top: 132px; width: 366px; height: 499px;
    background: linear-gradient(180deg, #0d2a5c 0%, #2c5f9e 45%, #c98a3e 80%, #1b355f 100%); }
  .section-title { font-size: 35px; font-weight: 600; color: var(--navy); letter-spacing: 0.5px; }
  .about-title { left: 413px; top: 27px; }
  .about-body { left: 413px; top: 86px; width: 680px; font-size: 16.5px; line-height: 26px; }
  .about-body p + p { margin-top: 26px; }

  /* Video band */
  .video-band { left: 0; top: 1127px; width: 1200px; height: 435px;
    background: linear-gradient(90deg, #c8dbe8 0%, #e6ecef 40%, #f3e7cf 60%, #b7cee0 100%); }
  .video-tile { top: 1170px; height: 342px; display: flex; align-items: center; justify-content: center; gap: 12px; color: var(--white); font-size: 33px; font-weight: 700; }
  .video-tile.one { left: 41px; width: 552px; background: linear-gradient(135deg, #2f5f9d 0%, #4f82b9 50%, #2a4f86 100%); }
  .video-tile.two { left: 605px; width: 554px; background: linear-gradient(180deg, #7fa9cf 0%, #4e7fb2 50%, #345e93 100%); }

  /* Mission */
  .mission-card { left: 41px; top: 1599px; width: 1118px; height: 558px; }
  .mission-photo { left: 752px; top: 0; width: 366px; height: 558px;
    background: linear-gradient(180deg, #2a3b55 0%, #6d6a72 35%, #e59a4a 62%, #3b4a63 100%); }
  .statement { left: 36px; width: 640px; }
  .statement p { font-size: 16.5px; line-height: 26px; margin-top: 14px; }

  /* Contact band */
  .touch-band { left: 0; top: 2206px; width: 1200px; height: 611px;
    background: linear-gradient(90deg, #35578a 0%, #5c80ae 45%, #4e72a3 100%); }
  .touch-title { left: 0; top: 2250px; width: 1200px; text-align: center; color: var(--white); font-size: 36px; font-weight: 700; }
  .form-card { left: 135px; top: 2319px; width: 598px; height: 445px; background: var(--white); box-shadow: var(--panel-shadow); }
  .form-heading { left: 55px; top: 56px; font-size: 24px; font-weight: 600; color: var(--navy); }
  .form-icon { left: 485px; top: 54px; }
  .field { width: 212px; border-bottom: 1px solid var(--field-line); font-size: 12px; color: var(--muted); padding-bottom: 4px; }
  .send-btn { left: 431px; top: 322px; width: 107px; height: 57px; background: var(--orange); display: flex; align-items: center; justify-content: center; }
  .info-panel { left: 733px; top: 2319px; width: 330px; height: 445px; background: rgba(108, 146, 200, 0.75); color: var(--white); }
  .info-heading { left: 53px; top: 56px; font-size: 23px; font-weight: 600; }
  .info-row { left: 47px; display: flex; align-items: flex-start; gap: 22px; font-size: 15px; line-height: 19px; color: #e8eef7; }
  .info-social { left: 68px; top: 366px; display: flex; gap: 17px; }
  .info-social span { width: 36px; height: 36px; border: 2px solid var(--white); display: block; }

  /* Footer */
  .site-footer .brand { left: 0; width: 1200px; top: 2847px; justify-content: center; font-size: 30px; }
  .copyright { left: 0; top: 2906px; width: 1200px; text-align: center; font-size: 16px; font-weight: 500; color: var(--navy); }
</style>
</head>
<body>

  <div class="abs hero" role="img" aria-label="Engineer in hard hat overlaid on an offshore oil platform at sunset"></div>

  <header class="site-header">
    <div class="abs brand"><span class="brand-mark"></span><span class="brand-name">MARENDO<small>CONSULTANTS</small></span></div>
    <nav class="abs nav">
      <a style="left:0">HOME</a>
      <a class="active" style="left:73px">ABOUT US</a>
      <a style="left:177px">SERVICES</a>
      <a style="left:275px">PORTFOLIO</a>
    </nav>
    <div class="abs contact-btn">CONTACT US</div>
    <div class="abs header-mail">
      <svg width="26" height="18" viewBox="0 0 26 18"><rect x="1" y="1" width="24" height="16" fill="var(--navy)"/><path d="M1 1 L13 10 L25 1" stroke="#fff" stroke-width="2" fill="none"/></svg>
      sample@email.com
    </div>
    <div class="abs header-social"><span></span><span></span><span></span><span></span></div>
  </header>

  <section class="abs card about-card">
    <div class="abs about-logo"><div class="brand"><span class="brand-mark"></span><span class="brand-name">MARENDO<small>CONSULTANTS</small></span></div></div>
    <div class="abs about-photo" role="img" aria-label="Refinery tower lit up at night"></div>
    <h1 class="abs section-title about-title">ABOUT US</h1>
    <div class="abs about-body">
      <p>Lorem Ipsum is simply dummy text of the printing and typesetting industry. Lorem Ipsum has been the industry's standard dummy text ever since the 1500s, when an unknown printer took a galley of type and scrambled it to make a type specimen book. It has survived not only five centuries,</p>
      <p>but also the leap into electronic typesetting, remaining essentially unchanged. It was popularised in the 1960s with the release of Tansheet sheets containing Lorem Ipsum passages, and more recently with desktop publishing software like Folio Layout including versions of Lorem Ipsum.</p>
      <p>Contrary to popular belief, Lorem Ipsum is not simply random text. It has roots in a piece of classical Latin literature from 45 BC, making it over 2000 years old. Edwin Harlow, a Latin professor at Ashgrove College in Virginia, looked up one of the more obscure Latin words,</p>
      <p>It is a long established fact that a reader will be distracted by the readable content of a page when looking at its layout. The point of using Lorem Ipsum is that it has a more-or-less normal distribution of letters, as opposed to using 'Content here, content here', making it look like readable English.</p>
    </div>
  </section>

  <section>
    <div class="abs video-band" role="img" aria-label="Faded industrial plant and pipelines in blue and sand tones"></div>
    <div class="abs video-tile one" role="img" aria-label="Engineer using a tablet in a control room">Watch video
      <svg width="80" height="80" viewBox="0 0 80 80"><circle cx="40" cy="40" r="37" stroke="#fff" stroke-width="4" fill="none"/><path d="M31 23 L58 40 L31 57 Z" fill="#fff"/></svg>
    </div>
    <div class="abs video-tile two" role="img" aria-label="Refinery pipelines under a blue sky">Watch video
      <svg width="80" height="80" viewBox="0 0 80 80"><circle cx="40" cy="40" r="37" stroke="#fff" stroke-width="4" fill="none"/><path d="M31 23 L58 40 L31 57 Z" fill="#fff"/></svg>
    </div>
  </section>

  <section class="abs card mission-card">
    <div class="abs statement" style="top:30px">
      <h2 class="section-title">OUR MISSION</h2>
      <p>Our mission is to provide responsive and unrivalled professional advice from learned and experienced&nbsp; professionals versed in the local market, with an understanding of the cultural and logistical challenges faced by foreign investors.</p>
    </div>
    <div class="abs statement" style="top:223px">
      <h2 class="section-title">OUR VISION</h2>
      <p>Our vision is to provide a complete investor's package that initiates with company registration, compliance and documentation services and ultimately operational facilitation services.</p>
    </div>
    <div class="abs statement" style="top:389px">
      <h2 class="section-title">OUR VISION</h2>
      <p>Our vision is to provide a complete investor's package that initiates with company registration, compliance and documentation services and ultimately operational facilitation services.</p>
    </div>
    <div class="abs mission-photo" role="img" aria-label="Power plant chimney reflected in water at sunset"></div>
  </section>

  <section>
    <div class="abs touch-band" role="img" aria-label="Blue-tinted industrial site with a hand on a laptop"></div>
    <h2 class="abs touch-title">GET IN TOUCH</h2>
    <div class="abs form-card">
      <h3 class="abs form-heading">Send us a message</h3>
      <svg class="abs form-icon" width="53" height="32" viewBox="0 0 53 32" fill="none" stroke="var(--orange)" stroke-width="2"><rect x="16" y="2" width="35" height="28"/><path d="M16 2 L33 17 L51 2"/><path d="M0 8 H11 M4 16 H11 M0 24 H11"/></svg>
      <div class="abs field" style="left:59px;top:142px">Enter your name</div>
      <div class="abs field" style="left:327px;top:142px">Enter your email</div>
      <div class="abs field" style="left:59px;top:243px">Enter your subject</div>
      <div class="abs field" style="left:327px;top:243px">Enter your phone number</div>
      <div class="abs field" style="left:59px;top:342px;width:180px">Enter your message</div>
      <div class="abs send-btn">
        <svg width="36" height="32" viewBox="0 0 36 32" fill="none" stroke="#fff" stroke-width="2" stroke-linejoin="round"><path d="M2 14 L34 2 L26 30 L16 20 Z M16 20 L34 2 M16 20 L15 29 L20 24"/></svg>
      </div>
    </div>
    <div class="abs info-panel">
      <h3 class="abs info-heading">Contact Information</h3>
      <div class="abs info-row" style="top:122px">
        <svg width="44" height="44" viewBox="0 0 44 44" fill="none" stroke="#fff" stroke-width="2"><path d="M22 32 C14 22 11 17 11 12 A11 11 0 0 1 33 12 C33 17 30 22 22 32 Z"/><circle cx="22" cy="12" r="4"/><path d="M13 28 L3 42 H41 L31 28"/></svg>
        <span>1234 Sample Address<br>Sample city</span>
      </div>
      <div class="abs info-row" style="top:203px">
        <svg width="44" height="42" viewBox="0 0 44 42" fill="none" stroke="#fff" stroke-width="2"><path d="M2 16 L22 2 L42 16 V40 H2 Z"/><path d="M2 16 L22 30 L42 16"/><circle cx="22" cy="16" r="5"/></svg>
        <span style="padding-top:10px">sample@email.com</span>
      </div>
      <div class="abs info-row" style="top:283px">
        <svg width="44" height="44" viewBox="0 0 44 44" fill="none" stroke="#fff" stroke-width="2" stroke-linejoin="round"><path d="M6 4 L14 2 L19 13 L13 17 C16 24 20 28 27 31 L31 25 L42 30 L40 38 C24 40 4 20 6 4 Z"/></svg>
        <span style="padding-top:10px">12345-567-34343</span>
      </div>
      <div class="abs info-social"><span></span><span></span><span></span><span></span></div>
    </div>
  </section>

  <footer class="site-footer">
    <div class="abs brand"><span class="brand-mark" style="width:30px;height:30px"></span><span class="brand-name">MARENDO<small>CONSULTANTS</small></span></div>
    <p class="abs copyright">Copyright © 218 - Marendo Consultant</p>
  </footer>

</body>
</html>
```